Auto Insurance Flyer

Target Market(s)

english/spanish

Industry/Entity Type

Insurance Broker

Font styles to use
Serif

Colors

Designer to choose colors to be used in the design.

Requirements
Must have
• blend with my logo colors
Nice to have
• Eye catching call to action. Attention grabbers

```html
<!DOCTYPE html>
<html lang="en">
<head>
<meta charset="utf-8">
<title>Auto Insurance Flyer – English / Spanish</title>
<link href="https://fonts.googleapis.com/css2?family=Montserrat:wght@300;400;500;700;800&display=swap" rel="stylesheet">
<style>
  :root {
    --ink: #000000;
    --panel: #1f5f7d;
    --panel-light: #2f7596;
    --white: #ffffff;
    --brand-gold: #a8875a;
    --card-warm: #c77a45;
    --card-pale: #eef2f6;
  }
  * { box-sizing: border-box; margin: 0; padding: 0; }
  html, body {
    width: 844px; height: 1200px; overflow: hidden;
    background: var(--white);
    font-family: "Montserrat", sans-serif;
  }
  .sheet { position: relative; width: 844px; height: 1200px; }

  .language-label {
    position: absolute; left: 40px;
    font-size: 34px; font-weight: 800; color: var(--ink); line-height: 1;
  }
  .language-label--en { top: 32px; }
  .language-label--es { top: 622px; }

  .flyer {
    position: absolute; width: 763px; height: 493px;
    background: var(--panel); color: var(--white); overflow: hidden;
  }
  .flyer--en { left: 39px; top: 76px; }
  .flyer--es { left: 42px; top: 662px; }

  .flyer > * { position: absolute; }

  .car-artwork {
    left: 355px; top: 262px; width: 408px; height: 231px;
    background: linear-gradient(135deg, var(--panel-light), var(--panel) 55%, #3d86a6);
    border-radius: 120px 0 0 0;
    opacity: .8;
  }

  .headline { text-align: right; line-height: 1; white-space: nowrap; }
  .headline__main { top: 20px; font-size: 48px; font-weight: 300; }
  .headline__main strong { font-weight: 800; }
  .headline__sub { top: 74px; font-size: 40px; font-weight: 400; }
  .flyer--en .headline { right: 162px; }
  .flyer--es .headline { right: 161px; }
  .flyer--es .headline__main { font-size: 45px; top: 22px; }
  .flyer--es .headline__sub { top: 72px; }

  .brand-badge {
    left: 648px; top: 11px; width: 94px; height: 94px; border-radius: 50%;
    background: var(--white);
    display: flex; align-items: center; justify-content: center; text-align: center;
    color: var(--brand-gold); font-size: 10px; font-weight: 500; line-height: 1.25;
    letter-spacing: .4px; text-transform: uppercase;
  }

  .also-title { left: 27px; top: 118px; font-size: 24px; font-weight: 500; line-height: 1; }

  .coverage-list { left: 27px; top: 153px; list-style: none; }
  .coverage-list li {
    display: flex; align-items: center; gap: 17px;
    height: 26.5px; font-size: 17px; font-weight: 500;
  }
  .coverage-list svg { width: 17px; height: 17px; flex: none; }

  .phone-box {
    left: 533px; top: 150px; width: 232px; height: 68px;
    border: 1px solid var(--white); border-right: none;
    display: flex; align-items: center; gap: 16px; padding-left: 10px;
  }
  .phone-box svg { width: 36px; height: 36px; flex: none; }
  .phone-box__numbers { font-size: 19px; font-weight: 500; line-height: 22px; }

  .offer-text {
    left: 27px; width: 330px; font-size: 14px; font-weight: 400; line-height: 16.6px;
  }
  .offer-text strong { font-weight: 700; }
  .offer-text--coverage { top: 244px; }
  .offer-text--prequal { top: 335px; }
  .flyer--es .offer-text { font-size: 13.4px; width: 345px; }
  .flyer--es .offer-text--coverage { top: 234px; }
  .flyer--es .offer-text--prequal { top: 324px; }

  .benefit-cards { display: block; margin: 5px 0 0 174px; line-height: 0; white-space: nowrap; }
  .flyer--es .benefit-cards { display: inline-block; margin: 0 0 0 12px; vertical-align: top; }
  .benefit-card { display: inline-block; width: 42px; height: 27px; border-radius: 1px; margin-right: 4px; }
  .benefit-card--warm { background: linear-gradient(135deg, var(--card-warm), #7fa3b8); }
  .benefit-card--pale { background: var(--card-pale); }

  .quote-cta { left: 27px; top: 423px; display: flex; align-items: center; gap: 10px; }
  .quote-cta svg { width: 34px; height: 34px; flex: none; }
  .quote-cta__label { font-size: 15px; font-weight: 400; line-height: 18px; }
  .quote-cta__url { font-size: 15px; font-weight: 500; line-height: 18px; }
  .flyer--es .quote-cta__label { font-size: 12.5px; }

  .office-list { left: 27px; top: 474px; font-size: 11px; font-weight: 400; }
</style>
</head>
<body>
<main class="sheet">

  <h2 class="language-label language-label--en">English</h2>
  <section class="flyer flyer--en" lang="en">
    <div class="car-artwork" role="img" aria-label="Line illustration of a classic car seen from the front three-quarter angle"></div>

    <h1 class="headline headline__main">Drive with <strong>confidence!</strong></h1>
    <p class="headline headline__sub">Let us insure it</p>

    <div class="brand-badge">Harbor Crest<br>Insurance<br>Services</div>

    <h3 class="also-title">Also:</h3>
    <ul class="coverage-list">
      <li><svg viewBox="0 0 20 20"><circle cx="10" cy="10" r="10" fill="#fff"/><path d="M5.5 10.3l3 3 6-6.3" fill="none" stroke="#1f5f7d" stroke-width="2.2"/></svg>Motorcycle insurance.</li>
      <li><svg viewBox="0 0 20 20"><circle cx="10" cy="10" r="10" fill="#fff"/><path d="M5.5 10.3l3 3 6-6.3" fill="none" stroke="#1f5f7d" stroke-width="2.2"/></svg>Renters insurance.</li>
      <li><svg viewBox="0 0 20 20"><circle cx="10" cy="10" r="10" fill="#fff"/><path d="M5.5 10.3l3 3 6-6.3" fill="none" stroke="#1f5f7d" stroke-width="2.2"/></svg>Homeowners insurance.</li>
    </ul>

    <div class="phone-box">
      <svg viewBox="0 0 24 24"><path fill="#fff" d="M6.6 2.2c.6-.4 1.4-.3 1.8.3l2.2 3.3c.4.6.3 1.4-.2 1.9L9 9.1c.9 2.2 3.1 4.7 5.7 5.9l1.5-1.4c.5-.5 1.3-.5 1.900-.1l3.2 2.3c.6.4.7 1.3.3 1.9l-1.4 2c-.7 1-2 1.5-3.2 1.1C10.3 18.8 5 13.4 3 6.7c-.4-1.2 0-2.5 1-3.3z"/></svg>
      <div class="phone-box__numbers">925-555-0142<br>(510) 555-0187</div>
    </div>

    <p class="offer-text offer-text--coverage">We can provide full coverage, liability insurance and if you are having trouble affording car insurance please ask about our california state low cost insurance policy.</p>
    <p class="offer-text offer-text--prequal">If you have <strong>medical card</strong> and/or <strong>food stamp card</strong> then you are already <strong>pre qualified</strong>.
      <span class="benefit-cards"><span class="benefit-card benefit-card--warm" role="img" aria-label="Food assistance card"></span><span class="benefit-card benefit-card--pale" role="img" aria-label="State medical benefits card"></span></span>
    </p>

    <div class="quote-cta">
      <svg viewBox="0 0 34 34" fill="none" stroke="#fff" stroke-width="1.8"><circle cx="15" cy="15" r="13"/><ellipse cx="15" cy="15" rx="6" ry="13"/><path d="M2 15h26M4 8h22M4 22h22"/><path d="M23 22l9 4-4 1.5-1.5 4z" fill="#fff"/></svg>
      <div>
        <div class="quote-cta__label">Request a quote on our website:</div>
        <div class="quote-cta__url">www.harborcrestinsurance.com</div>
      </div>
    </div>

    <p class="office-list">Offices in Oakland, Concord, Pittsburg, Antioch and Brentwood</p>
  </section>

  <h2 class="language-label language-label--es">Spanish</h2>
  <section class="flyer flyer--es" lang="es">
    <div class="car-artwork" role="img" aria-label="Ilustración de línea de un auto clásico visto de frente en ángulo"></div>

    <h1 class="headline headline__main">Conduzca con <strong>confianza.</strong></h1>
    <p class="headline headline__sub">Asegúrese.</p>

    <div class="brand-badge">Harbor Crest<br>Insurance<br>Services</div>

    <h3 class="also-title">También para:</h3>
    <ul class="coverage-list">
      <li><svg viewBox="0 0 20 20"><circle cx="10" cy="10" r="10" fill="#fff"/><path d="M5.5 10.3l3 3 6-6.3" fill="none" stroke="#1f5f7d" stroke-width="2.2"/></svg>Motocicletas.</li>
      <li><svg viewBox="0 0 20 20"><circle cx="10" cy="10" r="10" fill="#fff"/><path d="M5.5 10.3l3 3 6-6.3" fill="none" stroke="#1f5f7d" stroke-width="2.2"/></svg>Inquilinos.</li>
      <li><svg viewBox="0 0 20 20"><circle cx="10" cy="10" r="10" fill="#fff"/><path d="M5.5 10.3l3 3 6-6.3" fill="none" stroke="#1f5f7d" stroke-width="2.2"/></svg>Propietarios de viviendas.</li>
    </ul>

    <div class="phone-box">
      <svg viewBox="0 0 24 24"><path fill="#fff" d="M6.6 2.2c.6-.4 1.4-.3 1.8.3l2.2 3.3c.4.6.3 1.4-.2 1.9L9 9.1c.9 2.2 3.1 4.7 5.7 5.9l1.5-1.4c.5-.5 1.3-.5 1.9-.1l3.2 2.3c.6.4.7 1.3.3 1.9l-1.4 2c-.7 1-2 1.5-3.2 1.1C10.3 18.8 5 13.4 3 6.7c-.4-1.2 0-2.5 1-3.3z"/></svg>
      <div class="phone-box__numbers">925-555-0142<br>(510) 555-0187</div>
    </div>

    <p class="offer-text offer-text--coverage">Podemos proporcionar cobertura total, seguro de responsabilidad civil y si está teniendo problemas para pagar el seguro del vehículo consulte nuestra póliza de seguro de bajo costo del estado de California.</p>
    <p class="offer-text offer-text--prequal">Si tiene una <strong>tarjeta médica</strong> y/o <strong>una tarjeta de cupones para alimentos</strong>, entonces ya está <strong>precalificado.</strong><span class="benefit-cards"><span class="benefit-card benefit-card--warm" role="img" aria-label="Tarjeta de asistencia alimentaria"></span><span class="benefit-card benefit-card--pale" role="img" aria-label="Tarjeta de beneficios médicos del estado"></span></span></p>

    <div class="quote-cta">
      <svg viewBox="0 0 34 34" fill="none" stroke="#fff" stroke-width="1.8"><circle cx="15" cy="15" r="13"/><ellipse cx="15" cy="15" rx="6" ry="13"/><path d="M2 15h26M4 8h22M4 22h22"/><path d="M23 22l9 4-4 1.5-1.5 4z" fill="#fff"/></svg>
      <div>
        <div class="quote-cta__label">Solicite un presupuesto en nuestra web:</div>
        <div class="quote-cta__url">www.seguros-harborcrest.com</div>
      </div>
    </div>

    <p class="office-list">Oficinas en Oakland, Concord, Pittsburg, Antioch y Brentwood.</p>
  </section>

</main>
</body>
</html>
```